Coffee bag stamp design for new coffee brand

Stamp design that will be used like a label on a coffee package.
It must be a vector that can be produced as a stamp. Coffee bag is from brown craft paper. I upload image of this bag. Size of design is 80mm x 140mm.
I also uploaded two pictures for inspiration, but I will also appreciate new ideas.

Target Market(s)

Coffee lovers, who love to try new coffee. Also hipsters.

Colors

Designer to choose only greyscale colors for use in the design.

Requirements
Must have
• Some information about coffee must have:
Name: BRAZIL (the biggest font in that design)
Region: Santos
Altitude: 60 – 1200 m.n.m.
Variety: Arabica
Processing: unwashed

```html
<!DOCTYPE html>
<html lang="en">
<head>
<meta charset="utf-8">
<title>Brazil Santos – Coffee Bag Stamp</title>
<link href="https://fonts.googleapis.com/css2?family=Alfa+Slab+One&family=Barlow+Condensed:wght@500&family=Montserrat:wght@800&display=swap" rel="stylesheet">
<style>
  :root {
    --paper: #ead3c1;
    --ink: #2b2b2b;
    --ink-soft: #5a5a5a;
    --ink-light: #ffffff;
  }
  * { margin: 0; padding: 0; box-sizing: border-box; }
  html, body { width: 1125px; height: 1200px; overflow: hidden; }
  body { background: var(--paper); position: relative; color: var(--ink); }

  .stamp { position: absolute; inset: 0; }

  .stamp-emblem { position: absolute; left: 0; top: 0; width: 1125px; height: 680px; }
  .origin-name {
    font-family: "Alfa Slab One", serif;
    font-size: 94px;
    letter-spacing: 10px;
    fill: var(--ink);
  }
  .brand-name, .brand-sub {
    font-family: "Montserrat", sans-serif;
    font-weight: 800;
    fill: var(--ink);
  }
  .brand-name { font-size: 60px; }
  .brand-sub { font-size: 38px; letter-spacing: 2px; }

  .region {
    position: absolute; left: 272px; top: 592px; width: 580px;
    text-align: center; white-space: nowrap;
    font-family: "Montserrat", sans-serif; font-weight: 800;
    font-size: 42px; letter-spacing: 1px;
  }

  .altitude-table {
    position: absolute; left: 272px; top: 659px; width: 580px; height: 74px;
    display: flex; border: 4px solid var(--ink);
    font-family: "Barlow Condensed", sans-serif; font-weight: 500; font-size: 50px;
  }
  .altitude-table .cell {
    display: flex; align-items: center; justify-content: center;
    border-right: 4px solid var(--ink); white-space: nowrap;
  }
  .altitude-table .cell:last-child { border-right: 0; }
  .cell-label { width: 222px; }
  .cell-low { width: 84px; }
  .cell-high { flex: 1; }

  .landscape-art {
    position: absolute; left: 272px; top: 745px; width: 580px; height: 270px;
    background: linear-gradient(180deg, rgba(90,90,90,0.10), rgba(90,90,90,0.28));
  }

  .variety {
    position: absolute; left: 242px; top: 1022px; width: 640px;
    text-align: center; white-space: nowrap;
    font-family: "Alfa Slab One", serif; font-weight: 400;
    font-size: 45px; letter-spacing: 1px; line-height: 60px;
  }

  .processing {
    position: absolute; left: 272px; top: 1090px; width: 580px; height: 70px;
    background: var(--ink); color: var(--ink-light);
    display: flex; align-items: center; justify-content: center; white-space: nowrap;
    font-family: "Montserrat", sans-serif; font-weight: 800; font-size: 31px; letter-spacing: 1px;
  }
</style>
</head>
<body>
  <main class="stamp">
    <svg class="stamp-emblem" viewBox="0 0 1125 680" xmlns="http://www.w3.org/2000/svg">
      <defs>
        <radialGradient id="burst-tone" cx="50%" cy="50%" r="50%">
          <stop offset="0.5" stop-color="#5a5a5a" stop-opacity="0.28"/>
          <stop offset="1" stop-color="#5a5a5a" stop-opacity="0"/>
        </radialGradient>
        <path id="origin-arc" d="M 322 380 A 240 240 0 0 1 802 380"/>
      </defs>
      <circle class="sunburst" role="img" aria-label="Sunburst of radiating lines behind the emblem" cx="562" cy="370" r="290" fill="url(#burst-tone)"/>
      <circle class="brand-ring" cx="562" cy="370" r="150" fill="var(--paper)" stroke="var(--ink)" stroke-width="9"/>
      <text class="origin-name"><textPath href="#origin-arc" startOffset="50%" text-anchor="middle">BRAZIL</textPath></text>
      <text class="brand-name" x="562" y="382" text-anchor="middle">KAVIRA</text>
      <text class="brand-sub" x="562" y="430" text-anchor="middle">COFFEE</text>
    </svg>

    <h2 class="region">REGION: SANTOS</h2>

    <div class="altitude-table">
      <div class="cell cell-label">ALTITUDE</div>
      <div class="cell cell-low">60</div>
      <div class="cell cell-high">1200 M.N.M.</div>
    </div>

    <div class="landscape-art" role="img" aria-label="Line illustration of a coffee plantation with rows leading to the horizon, coffee plants and buildings on both sides"></div>

    <h3 class="variety">VARIETY: ARABICA</h3>

    <div class="processing">PROCESSING: UNWASHED</div>
  </main>
</body>
</html>
```